KRV Affirmation and Intention Card Design

I would like to have designs created that will be used on my Affirmation and Intention Cards I will be selling. We are a luxury brand. The designs need to be aesthetically pleasing, but minimal (think blush pinks/matte blacks/cream/warm earth tones/teals with gold/rose gold/silver lettering and visuals. Intention cards will have the same intentions as the inspiration photo. Affirmation cards will have random inspirational and biblical quotes. I only need two designs for the back of the Affirmation cards. One for design for every day quotes and one design for biblical quotes. For the intentions cards I would like a design for one side of card that will be on all cards and on the other side a design that correlates with each intention. See inspiration photo attached.

Target Market(s)

Millennials/ Women/ Similiar to Inspiration Photos below. Design that will look well on any color card stock I choose.

Industry/Entity Type

Lifestyle

Requirements
Must have
• Design that can fit on cards approximately 4 x 2.5 or 4x3 or 3.5 x 2.5 in size

```html
<!DOCTYPE html>
<html lang="en">
<head>
<meta charset="utf-8">
<title>Affirmation and Intention Cards</title>
<link rel="stylesheet" href="https://fonts.googleapis.com/css2?family=Playfair+Display:wght@700;800&display=swap">
<style>
  :root {
    --backdrop: #e4e4e4;
    --blush: #f5b7d3;
    --peach: #f0a596;
    --ink: #ffffff;
    --ink-soft: rgba(255, 255, 255, 0.92);
  }
  * { box-sizing: border-box; margin: 0; padding: 0; }
  html, body { width: 891px; height: 1200px; overflow: hidden; }
  body {
    background: var(--backdrop);
    font-family: "Playfair Display", Georgia, serif;
    color: var(--ink);
    position: relative;
  }
  .card {
    position: absolute;
    top: 300px;
    width: 400px;
    height: 590px;
    background:
      radial-gradient(ellipse 62% 48% at 50% 46%, var(--peach) 0%, rgba(240,165,150,0.55) 45%, rgba(245,183,211,0) 100%),
      var(--blush);
  }
  .card--quote { left: 30px; }
  .card--intention { left: 461px; }
  .card__frame {
    position: absolute;
    inset: 14px;
    border: 2px solid var(--ink);
  }
  .card__title {
    position: absolute;
    left: 30px; right: 30px;
    text-align: center;
    font-weight: 800;
    font-size: 34px;
    line-height: 1.1;
  }
  .card--quote .card__title { top: 70px; }
  .card--intention .card__title { top: 48px; font-size: 30px; }
  .card__art {
    position: absolute;
    left: 50%;
    transform: translateX(-50%);
    border-radius: 50%;
    background: radial-gradient(circle, rgba(240,150,135,0.85) 0%, rgba(240,165,150,0.45) 45%, rgba(245,183,211,0) 75%);
  }
  .card--quote .card__art { top: 140px; width: 300px; height: 300px; opacity: 0.6; }
  .card--intention .card__art { top: 110px; width: 320px; height: 320px; }
  .quote-mark {
    position: absolute;
    left: 0; right: 0;
    text-align: center;
    font-weight: 800;
    font-size: 64px;
    line-height: 1;
    height: 40px;
  }
  .quote-mark--open { top: 170px; }
  .quote-mark--close { top: 390px; }
  .card__body {
    position: absolute;
    left: 30px; right: 30px;
    text-align: center;
    font-weight: 700;
    font-size: 16px;
    line-height: 1.45;
    color: var(--ink-soft);
  }
  .card--quote .card__body { top: 250px; }
  .card--intention .card__body { top: 450px; }
</style>
</head>
<body>
  <article class="card card--quote">
    <div class="card__frame"></div>
    <div class="card__art" role="img" aria-label="Faint line illustration of a sun with rays above an open hand and small stars"></div>
    <h2 class="card__title">Lorem ipsum dolor</h2>
    <span class="quote-mark quote-mark--open" aria-hidden="true">“</span>
    <p class="card__body">Lorem ipsum dolor sit amet, consectetuer<br>adipiscing elit, sed diam nonummy nibh<br>euismod tincidunt ut laoreet dolore<br>magna aliquam erat volutpat.</p>
    <span class="quote-mark quote-mark--close" aria-hidden="true">”</span>
  </article>

  <article class="card card--intention">
    <div class="card__frame"></div>
    <h2 class="card__title">Lorem ipsum</h2>
    <div class="card__art" role="img" aria-label="Line illustration of a radiant sun held above an open hand with sparkling stars"></div>
    <p class="card__body">Lorem ipsum dolor sit amet, consectetuer<br>adipiscing elit, sed diam nonummy nibh<br>euismod tincidunt ut laoreet dolore<br>magna aliquam erat volutpat.</p>
  </article>
</body>
</html>
```